Retail Package for Ammunition Company

We are looking for a packaging design for a retail boxed ammunition. The "look". Attached will be logo to be used. Box to represent strength and accuracy. Will need to provide .psd files to allow in house person to add/remove text to other calibers and warnings.

Browse Other Brands: http://www.brightcartridge.example/brands

The packaging needs to include:
Logo- provided and the following text:

FRONT 1. 9mm 115gr FMJ

BACK 2. WARNING: To avoid serious injury: (1) use only ammunition in good condition; use only in modern firearms in good condition marked for .22 Long Rifle (LR) cartridges; (2) always be sure barrel is free of any obstructions; the barrel should be checked in case of light recoil, or an unusually loud or weak sound heard during firing; (3) wear eye and ear protection; (4) if gun fails to fire, avoid exposure to breech when unloading and point muzzle in a safe direction. Keep firearm pointed in safe direction at all times; (5) discharge may occur if rim is struck; handle with caution, do not drop. (6) Do not shoot at hard surfaces or water to prevent ricochet; (7) Bullet is capable of traveling extreme distances. Know your backstop; (8) Store in cool dry place

3. LEAD WARNING: Discharging firearms in poorly ventilated areas, cleaning firearms, or handling ammunition may result in exposure to lead and other substances known to cause birth defects, reproductive harm, and other serious physical injury. Have adequate ventilation at all times. Wash hands thoroughly after exposure.

Dimensions ; (LxWxH): 5.25" x 2.625" x 1.125"

Target Market(s)

US Veterans, Gun and Ammo enthusiast. Military/Law Enforcement person.

Industry/Entity Type

Gun

Requirements
Must have
• Logo provided, text provided
Nice to have
• would like to see a package that looks better than the leaders, such as Halvorsen, TWP, Brackenford, Meltaro. .....just browse these brands: http://www.brightcartridge.example/brands
Should not have
• cartoonist style characters. No animals.

```html
<!DOCTYPE html>
<html lang="en">
<head>
<meta charset="utf-8">
<title>Ironvale Ammunition – 9mm Retail Box Dieline</title>
<link rel="stylesheet" href="https://fonts.googleapis.com/css2?family=Montserrat:wght@800&family=Archivo+Black&family=Arimo:wght@400;700&display=swap">
<style>
  :root{
    --backdrop:#e6e4e0;
    --navy:#1c335e;
    --navy-deep:#142645;
    --back-blue:#1f3a6b;
    --panel-black:#1a1a1a;
    --panel-dark:#222;
    --ink:#ffffff;
    --badge:#e8e8e8;
  }
  *{margin:0;padding:0;box-sizing:border-box}
  html,body{width:1200px;height:900px;overflow:hidden;background:var(--backdrop)}
  .canvas{position:relative;width:1200px;height:900px}
  .dieline{position:absolute;left:0;top:0}
  .body-text{font-family:"Arimo",Arial,sans-serif;color:var(--ink)}
  .brand{font-family:"Montserrat",Arial,sans-serif;font-weight:800;color:var(--ink);text-align:center;line-height:1}
  .lead-warning{position:absolute;left:405px;top:167px;width:356px;font-size:8.4px;line-height:10.4px}
  .lead-warning b{font-weight:700}
  .front-brand{position:absolute;left:410px;top:286px;width:380px}
  .front-brand .name{font-size:66px;letter-spacing:-1px}
  .front-brand .sub{font-size:22px;letter-spacing:17px;margin-top:6px;padding-left:17px}
  .side-brand{position:absolute;width:160px;transform:rotate(-90deg);transform-origin:center}
  .side-brand .name{font-size:30px;letter-spacing:-0.5px}
  .side-brand .sub{font-size:8px;letter-spacing:7px;margin-top:3px;padding-left:7px}
  .side-left{left:250px;top:328px}
  .side-right{left:760px;top:328px}
  .caliber{position:absolute;left:436px;top:416px;width:320px;text-align:center;font-family:"Archivo Black",Arial,sans-serif;font-size:16.5px;color:var(--ink)}
  .front-warning{position:absolute;left:436px;top:436px;width:320px;text-align:center;font-size:7.2px;font-weight:700}
  .back-heading{position:absolute;left:403px;top:554px;font-size:14.5px}
  .back-heading b{font-weight:700}
  .warn-col{position:absolute;font-size:7.2px;line-height:9.3px}
  .warn-col p{margin-bottom:9.3px}
  .warn-col-a{left:391px;top:595px;width:186px}
  .warn-col-b{left:582px;top:595px;width:150px}
  .back-brand{position:absolute;left:596px;top:704px;width:146px}
  .back-brand .name{font-size:25px;letter-spacing:-0.5px}
  .back-brand .sub{font-size:7px;letter-spacing:6.5px;margin-top:2px;padding-left:6px}
</style>
</head>
<body>
<main class="canvas">
  <svg class="dieline" width="1200" height="900" viewBox="0 0 1200 900" xmlns="http://www.w3.org/2000/svg">
    <defs>
      <linearGradient id="navyFade" x1="0" y1="0" x2="1" y2="1">
        <stop offset="0" stop-color="#1e3766"/>
        <stop offset="1" stop-color="#172c52"/>
      </linearGradient>
      <linearGradient id="blackFade" x1="0" y1="0" x2="0" y2="1">
        <stop offset="0" stop-color="#111"/>
        <stop offset="0.5" stop-color="#262626"/>
        <stop offset="1" stop-color="#151515"/>
      </linearGradient>
    </defs>
    <!-- top flap -->
    <polygon class="flap-top" points="286,150 886,150 886,208 800,230 796,240 376,240 372,230 286,208" fill="url(#navyFade)"/>
    <!-- side panels -->
    <polygon class="side-panel" points="286,240 376,240 376,452 286,452" fill="url(#navyFade)"/>
    <polygon class="side-panel" points="796,240 886,240 886,452 796,452" fill="url(#navyFade)"/>
    <!-- lower tabs -->
    <polygon class="tab" points="286,468 372,462 376,470 376,530 286,530" fill="url(#navyFade)"/>
    <polygon class="tab" points="796,470 800,462 886,468 886,530 796,530" fill="url(#navyFade)"/>
    <!-- front panel -->
    <rect class="front-panel" x="376" y="240" width="420" height="300" fill="url(#blackFade)"/>
    <polygon class="front-band" points="392,240 796,240 796,410 436,410" fill="url(#navyFade)"/>
    <!-- back panel -->
    <rect class="back-panel" x="376" y="540" width="420" height="210" fill="#1b1b1b"/>
    <path class="back-band" d="M376,584 L736,584 Q746,584 750,596 L778,750 L376,750 Z" fill="var(--back-blue)"/>
    <!-- origin badge, plain -->
    <circle class="origin-badge" cx="413" cy="416" r="23" fill="none" stroke="var(--badge)" stroke-width="2"/>
  </svg>

  <p class="lead-warning body-text"><b>LEAD WARNING:</b> Discharging firearms in poorly ventilated areas, cleaning firearms, or handling ammunition may result in exposure to lead and other substances known to cause birth defects, reproductive harm, and other serious physical injury. Have adequate ventilation at all times. Wash hands thoroughly after exposure.</p>

  <div class="brand side-brand side-left"><div class="name">IRONVALE</div><div class="sub">AMMUNITION</div></div>
  <div class="brand side-brand side-right"><div class="name">IRONVALE</div><div class="sub">AMMUNITION</div></div>

  <div class="brand front-brand"><div class="name">IRONVALE</div><div class="sub">AMMUNITION</div></div>

  <h1 class="caliber">9mm (9x19mm) 115gr FMJ</h1>
  <p class="front-warning body-text">WARNING : Keep out of reach of children. Read all warnings on package</p>

  <h2 class="back-heading body-text"><b>WARNING:</b> To avoid serious injury:</h2>
  <div class="warn-col warn-col-a body-text">
    <p>1) use only ammunition in good condition; use only in modern firearms in good condition marked for .22 Long Rifle (LR) cartridges;</p>
    <p>(2) always be sure barrel is free of any obstructions; the barrel should be checked in case of light recoil, or an unusually loud or weak sound heard during firing;</p>
    <p>(3) wear eye and ear protection;</p>
    <p>(4) if gun fails to fire, avoid exposure to breech when unloading and point muzzle in a safe direction. Keep firearm pointed in safe direction at all times;</p>
  </div>
  <div class="warn-col warn-col-b body-text">
    <p>(5) discharge may occur if rim is struck; handle with caution, do not drop.</p>
    <p>(6) Do not shoot at hard surfaces or water to prevent ricochet;</p>
    <p>(7) Bullet is capable of traveling extreme distances. Know your backstop;</p>
    <p>(8) Store in cool dry place</p>
  </div>
  <div class="brand back-brand"><div class="name">IRONVALE</div><div class="sub">AMMUNITION</div></div>
</main>
</body>
</html>
```